Chestnut Farm Logo and Business Card

We need a new logo design and new business cards for a recently purchased mature Chestnut Farm in the south west of Western Australia, the farm is called Willowmere Glen, We will be adding value to the chestnuts by creating a range of chestnut products based on the fact that chestnuts are a healthy, gluten free product that is suited to the vegetarian market as well as the health food market. We will be selling the products through farmers markets, restaurants, health food stores and online. The final design should communicate a healthy modern down to earth image.
Updates

Sorry, I should have given the details for the business cards.

Address is 
Willowmere Glen
PO Box 417 
Kerriford, Tallowood District, 6318

Email is 
willowmere.glen@fernpost.com

Website is
www.glenhollowfoods.com

Phone number is 
(08) 9412 7730

Many thanks

We would like to see the logo separate to the business card as well if possible please?

Industry/Entity Type

Farm

Logo Text

Willowmere Glen

```html
<!DOCTYPE html>
<html lang="en">
<head>
<meta charset="utf-8">
<title>Willowmere Glen – Business Card</title>
<link rel="stylesheet" href="https://fonts.googleapis.com/css2?family=Questrial&display=swap">
<style>
  :root {
    --backdrop: #d9d9d9;
    --card-white: #ffffff;
    --maroon: #5a1512;
    --maroon-deep: #4a0f0d;
    --leaf-green: #2e9a3a;
    --leaf-dark: #1d7a2a;
    --brand-brown: #5b1a14;
    --ink-light: #ffffff;
  }
  * { box-sizing: border-box; margin: 0; padding: 0; }
  html, body {
    width: 1200px; height: 900px; overflow: hidden;
    background: var(--backdrop);
    font-family: "Questrial", "Century Gothic", sans-serif;
  }
  .canvas {
    width: 1200px; height: 900px;
    display: flex; align-items: center; justify-content: center;
  }
  .business-card {
    position: relative;
    width: 960px; height: 585px;
    border-radius: 44px;
    overflow: hidden;
    background: var(--card-white);
    box-shadow: 0 18px 40px rgba(0,0,0,0.18);
  }
  .brand-area {
    position: absolute; left: 0; top: 0; right: 0; height: 278px;
    display: flex; align-items: center; justify-content: center;
    gap: 26px; padding-top: 40px;
  }
  .brand-mark {
    width: 70px; height: 70px; border-radius: 50%;
    background: var(--leaf-green);
    flex: none;
  }
  .brand-name {
    font-size: 84px; line-height: 1; font-weight: 400;
    color: var(--brand-brown);
    letter-spacing: 1px;
  }
  .divider-band {
    position: absolute; left: 0; right: 0; top: 278px; height: 20px;
    background: linear-gradient(var(--leaf-green), var(--leaf-dark));
  }
  .contact-panel {
    position: absolute; left: 0; right: 0; top: 298px; bottom: 0;
    background: linear-gradient(var(--maroon), var(--maroon-deep));
    padding: 38px 0 0 62px;
  }
  .contact-list { list-style: none; color: var(--ink-light); }
  .contact-item {
    display: flex; align-items: center; gap: 14px;
    font-size: 29px; line-height: 40px;
  }
  .contact-icon { width: 34px; height: 34px; flex: none; }
  .contact-item--continued { padding-left: 48px; }
</style>
</head>
<body>
<main class="canvas">
  <article class="business-card">
    <header class="brand-area">
      <span class="brand-mark" aria-hidden="true"></span>
      <h1 class="brand-name">Willowmere Glen</h1>
    </header>
    <div class="divider-band"></div>
    <section class="contact-panel">
      <ul class="contact-list">
        <li class="contact-item">
          <svg class="contact-icon" viewBox="0 0 24 24" aria-hidden="true">
            <path fill="#2e9a3a" d="M6.6 10.8a15 15 0 0 0 6.6 6.6l2.2-2.2c.3-.3.7-.4 1-.2 1.1.4 2.3.6 3.6.6.6 0 1 .4 1 1V20c0 .6-.4 1-1 1A17 17 0 0 1 3 4c0-.6.4-1 1-1h3.5c.6 0 1 .4 1 1 0 1.3.2 2.5.6 3.6.1.3 0 .7-.2 1z"/>
          </svg>
          <span>(08) 9412 7730</span>
        </li>
        <li class="contact-item">
          <svg class="contact-icon" viewBox="0 0 24 24" aria-hidden="true" fill="none" stroke="#2e9a3a" stroke-width="2">
            <circle cx="12" cy="12" r="9.5"/>
            <ellipse cx="12" cy="12" rx="4" ry="9.5"/>
            <path d="M2.5 12h19M4 7h16M4 17h16"/>
          </svg>
          <span>www.glenhollowfoods.com</span>
        </li>
        <li class="contact-item">
          <svg class="contact-icon" viewBox="0 0 24 24" aria-hidden="true">
            <rect x="2" y="5" width="20" height="14" rx="1.5" fill="#2e9a3a"/>
            <path d="M2.5 6l9.5 7 9.5-7" fill="none" stroke="#5a1512" stroke-width="1.6"/>
          </svg>
          <span>willowmere.glen@fernpost.com</span>
        </li>
        <li class="contact-item">
          <svg class="contact-icon" viewBox="0 0 24 24" aria-hidden="true">
            <path fill="#2e9a3a" d="M12 3 1.5 12h3v9h6v-6h3v6h6v-9h3z"/>
          </svg>
          <span>PO Box 417</span>
        </li>
        <li class="contact-item contact-item--continued">
          <span>Kerriford, Tallowood District, 6318</span>
        </li>
      </ul>
    </section>
  </article>
</main>
</body>
</html>
```